Business Card Design Project

Corvexa logo will be provided after
Front

Bram Oskarsen- Construction Manager

Ph: (61) 07 53182907
boskarsen@corvexa.com.au
PO Box 83 Kelbarra 4529

Back
Corvexa
EPCM

Oil - Gas - Mining

Industry/Entity Type

Business

Font styles to use
Sans Serif

Colors
faa54b

Requirements
Must have
• White Back Ground

```html
<!DOCTYPE html>
<html lang="en">
<head>
<meta charset="utf-8">
<title>Corvexa Business Cards</title>
<link href="https://fonts.googleapis.com/css2?family=Arimo:wght@400;700&display=swap" rel="stylesheet">
<style>
  :root {
    --accent: #faa54b;
    --ink: #111111;
    --paper: #ffffff;
    --card-black: #050505;
    --backdrop: #e9e7e4;
    --muted: #333333;
  }
  * { margin: 0; padding: 0; box-sizing: border-box; }
  html, body {
    width: 1200px; height: 960px; overflow: hidden;
    background: var(--backdrop);
    font-family: "Arimo", Arial, sans-serif;
  }
  .canvas {
    position: relative; width: 1200px; height: 960px;
    display: flex; flex-direction: column; align-items: center; justify-content: center; gap: 40px;
  }
  .card {
    position: relative; width: 700px; height: 400px;
    box-shadow: 0 6px 18px rgba(0,0,0,0.18);
  }
  /* Back side */
  .card-back { background: var(--card-black); color: var(--paper); }
  .back-brand {
    position: absolute; left: 0; right: 0; top: 140px;
    text-align: center;
  }
  .wordmark {
    font-weight: 700; letter-spacing: 4px; text-transform: uppercase;
  }
  .back-brand .wordmark { font-size: 64px; color: var(--paper); }
  .back-tagline {
    position: absolute; left: 330px; top: 232px;
    font-size: 17px; line-height: 1.45; color: var(--paper);
  }
  .back-tagline .service { display: block; padding-left: 34px; }
  .back-tagline .sep { margin: 0 8px; }

  /* Front side */
  .card-front { background: var(--paper); color: var(--ink); }
  .front-brand {
    position: absolute; left: 130px; top: 92px;
  }
  .front-brand .wordmark { font-size: 66px; color: var(--ink); }
  .person {
    position: absolute; left: 40px; top: 226px;
  }
  .person-name { font-size: 24px; font-weight: 700; color: var(--ink); }
  .person-title { font-size: 15px; color: var(--accent); margin-top: 2px; }
  .rule {
    position: absolute; left: 0; right: 0; top: 282px;
    height: 2px; background: var(--ink);
  }
  .contact {
    position: absolute; left: 40px; top: 318px;
    list-style: none; font-size: 14px; color: var(--muted);
  }
  .contact li, .address {
    display: flex; align-items: center; gap: 10px; height: 24px;
  }
  .address {
    position: absolute; right: 40px; top: 318px;
    font-size: 14px; color: var(--muted);
  }
  .icon {
    width: 16px; height: 16px; background: var(--accent);
    display: inline-flex; align-items: center; justify-content: center;
  }
  .icon svg { width: 11px; height: 11px; }
</style>
</head>
<body>
<main class="canvas">
  <section class="card card-back" aria-label="Card back">
    <div class="back-brand"><span class="wordmark">Corvexa</span></div>
    <p class="back-tagline">
      <span class="service">EPCM</span>
      Oil<span class="sep">|</span>Gas<span class="sep">|</span>Mining
    </p>
  </section>

  <section class="card card-front" aria-label="Card front">
    <div class="front-brand"><span class="wordmark">Corvexa</span></div>
    <div class="person">
      <p class="person-name">Bram Oskarsen</p>
      <p class="person-title">Construction Manager</p>
    </div>
    <div class="rule"></div>
    <ul class="contact">
      <li>
        <span class="icon"><svg viewBox="0 0 12 12"><path d="M2.5 1h2l1 2.5-1.3 1a6 6 0 0 0 3.3 3.3l1-1.3L11 7.5v2c0 .8-.7 1.5-1.5 1.5A8.5 8.5 0 0 1 1 2.5C1 1.7 1.7 1 2.5 1z" fill="#111"/></svg></span>
        (61) 07 53182907
      </li>
      <li>
        <span class="icon"><svg viewBox="0 0 12 12"><rect x="1" y="2.5" width="10" height="7" fill="none" stroke="#111" stroke-width="1.2"/><path d="M1 2.5l5 4 5-4" fill="none" stroke="#111" stroke-width="1.2"/></svg></span>
        boskarsen@corvexa.com.au
      </li>
    </ul>
    <p class="address">
      <span class="icon"><svg viewBox="0 0 12 12"><path d="M6 1a3.5 3.5 0 0 0-3.5 3.5C2.5 7.5 6 11 6 11s3.5-3.5 3.5-6.5A3.5 3.5 0 0 0 6 1z" fill="#111"/><circle cx="6" cy="4.5" r="1.3" fill="#faa54b"/></svg></span>
      PO Box 83 Kelbarra 4529
    </p>
  </section>
</main>
</body>
</html>
```